Tallow Salmon Labels

We need a graphic design label for a new product launch. Tallow is an 100% Australian family business specialised in making marinades made from natural and locally sourced fresh ingredients for fish and seafood. We make remarkable food for fine cooking prepared by hand at our kitchen in Condell Park, using the same ingredients and techniques you would use at home.

We are planning to launch three marinades for salmon.
The flavours are:

- Herb, Lemon & Cracked Black Pepper
- Ginger, Honey & Soy
- Coriander, Lemongrass, Shallot and Ginger

The marinades will be packed in a 300 grams clear pouch with spout and sold in the seafood section of a major retail supermarket.

Measurements of the pouch: 140 mm wide and 210 mm high but only 160 mm high from the spout downwards.

Label: For the label, It will be a 120mm wide X 120mm high If not slightly smaller. Please refer to File 2: to see the pouch.

The label will cover 75% of the front of the pouch and the marinade itself will be visible in the remaining 25 % of the pouch. The colours of the marinades are green for Herb, Lemon & Cracked Black Pepper and Coriander, Lemongrass, Shallot and Ginger; and dark brown for Ginger, Honey & Soy.

Our marinades do not contain additives. The marinades are Gluten free.

The label needs to visually communicate that the marinade is used for salmon.

Please choose a suitable typography for our name Tallow that communicates an artisan feel.

Please refer to File 1 as a guide to what we would like, but keep in mind we are very open to any ideas you may have.

Colours should reflect the nature of our business, as outlined above.
Updates

Hello Designers,

This is what the actual pouch looks like https://www.filecrate-example.net/sc/4kd9w2m7x1/Qa81Lpt3z_

We would like the label to be roughly 120mm X 120mm or within those parameters to fit the packaging.

Thank you!
- Moira

Hey Designers,

we have been looking at your designs and while we have liked some elements of them we would like to see more creativity with the actual graphics and shapes of the labels, different colour contrast and more clever and quirky designs. We want to make fish fun and interesting to consumers, something rustic that catches the eye but at the same time is still sophisticated and upmarket. 

We would like to see the following on your packaging designs:

- Pastels colours (green, blue and yellow).
- The 'Tallow gourmet' font to be in bolder typography
- An ink looking stamp for 'gluten free, no additives'
- Something about the product being hand crafted
- Must include the following text: Marinades made from natural and locally sourced fresh ingredients for fish and seafood

here are some examples for you to be inspired by

Some font ideas ..

http://pinboardly-example.net/pin/518203947716250341/
http://pinboardly-example.net/pin/73915268401837762/
http://pinboardly-example.net/pin/629450183027741856/
http://pinboardly-example.net/pin/384720615099214730/
http://pinboardly-example.net/pin/957301846620387412/
http://pinboardly-example.net/pin/140862397785023561/

colours/images/graphics

http://pinboardly-example.net/pin/803174529936610248/
http://pinboardly-example.net/pin/471028395512846307/
http://pinboardly-example.net/pin/695283017740158236/
http://pinboardly-example.net/pin/332610847958271649/ (We like this concept) 

Good luck! 

 

Target Market(s)

Home cooks, young professionals, anyone with a healthy eating lifestyle.

Industry/Entity Type

Graphic Design

Requirements
Must have
• The label needs to visually communicate that the marinade is used for salmon.
- Include "Gluten Free" and "No Additives" on the label
- Outline the freshness of the ingredients used in the marinade eg. Coriander, Lemongrass, Shallot and Ginger to be included on the label.
- Bright and eye catching colours (food friendly colours).
Nice to have
• - Open to pastel colours
- Vector drawings
Should not have
• - dull colours

```html
<!DOCTYPE html>
<html lang="en">
<head>
<meta charset="utf-8">
<title>Tallow Salmon Marinade Label</title>
<link rel="stylesheet" href="https://fonts.googleapis.com/css2?family=Oswald:wght@500&family=Cherry+Swash:wght@400;700&family=Parisienne&family=Federo&display=swap">
<style>
  :root {
    --page: #ffffff;
    --label-blue: #27a8e0;
    --frame-red: #e5433d;
    --salmon-light: #ec6a5c;
    --brand-navy: #2b3990;
    --cocoa: #5b3b1f;
    --lime: #d6e21f;
    --tick-rust: #a0602a;
    --hat-white: rgba(255, 255, 255, 0.85);
  }
  html, body {
    margin: 0;
    padding: 0;
    width: 1200px;
    height: 1200px;
    overflow: hidden;
    background: var(--page);
  }
  .label {
    position: absolute;
    left: 68px;
    top: 68px;
    width: 1057px;
    height: 1054px;
    background: var(--label-blue);
  }
  .frame {
    position: absolute;
    left: 0;
    top: 0;
    width: 1200px;
    height: 1200px;
  }
  .chef-hat {
    position: absolute;
    left: 505px;
    top: 140px;
    width: 180px;
    height: 140px;
    background: var(--hat-white);
    border-radius: 70px 70px 14px 14px;
    opacity: 0.35;
  }
  .brand-name {
    position: absolute;
    left: 0;
    width: 1200px;
    top: 288px;
    margin: 0;
    text-align: center;
    font-family: "Oswald", sans-serif;
    font-weight: 500;
    font-size: 178px;
    line-height: 1;
    letter-spacing: 2px;
    color: var(--brand-navy);
    transform: scaleX(0.6);
  }
  .product-name {
    position: absolute;
    left: 0;
    width: 1200px;
    top: 500px;
    margin: 0;
    text-align: center;
    font-family: "Cherry Swash", serif;
    font-weight: 400;
    font-size: 78px;
    line-height: 1;
    letter-spacing: 3px;
    color: var(--cocoa);
  }
  .flavour {
    position: absolute;
    left: 0;
    width: 1200px;
    top: 592px;
    margin: 0;
    text-align: center;
    font-family: "Parisienne", cursive;
    font-size: 58px;
    line-height: 1;
    color: var(--lime);
  }
  .salmon-art {
    position: absolute;
    left: 308px;
    top: 670px;
    width: 578px;
    height: 200px;
    border-radius: 24px;
    background: linear-gradient(90deg, var(--frame-red), var(--salmon-light) 50%, var(--frame-red));
  }
  .claims {
    position: absolute;
    left: 218px;
    top: 920px;
    margin: 0;
    padding: 0;
    list-style: none;
    font-family: "Federo", sans-serif;
    font-size: 24px;
    color: var(--cocoa);
  }
  .claims li {
    display: flex;
    align-items: center;
    gap: 12px;
    height: 48px;
  }
  .claims svg {
    width: 30px;
    height: 30px;
  }
  .freshness {
    position: absolute;
    left: 795px;
    top: 940px;
    margin: 0;
    font-family: "Cherry Swash", serif;
    font-size: 72px;
    line-height: 1;
    color: var(--lime);
  }
</style>
</head>
<body>
  <div class="label"></div>

  <svg class="frame" viewBox="0 0 1200 1200" aria-hidden="true">
    <g fill="none" stroke="var(--frame-red)" stroke-width="5" stroke-linecap="round">
      <circle cx="130" cy="130" r="32"/>
      <circle cx="1080" cy="128" r="32"/>
      <circle cx="130" cy="1032" r="32"/>
      <circle cx="1072" cy="1035" r="32"/>
      <path d="M150 102 Q600 150 1058 100"/>
      <path d="M160 1062 Q600 1100 1042 1064"/>
      <path d="M102 150 Q200 600 104 1010"/>
      <path d="M1108 150 Q1000 600 1100 1012"/>
    </g>
  </svg>

  <div class="chef-hat" role="img" aria-label="Chef's hat emblem"></div>

  <h1 class="brand-name">TALLOW</h1>
  <h2 class="product-name">salmon marinade</h2>
  <p class="flavour">Ginger, Honey &amp; Soy</p>

  <div class="salmon-art" role="img" aria-label="Hand-drawn red salmon illustration"></div>

  <ul class="claims">
    <li>
      <svg viewBox="0 0 30 30" aria-hidden="true"><path d="M4 16 L11 24 L27 5" fill="none" stroke="var(--tick-rust)" stroke-width="4" stroke-linecap="round" stroke-linejoin="round"/></svg>
      Gluten Free
    </li>
    <li>
      <svg viewBox="0 0 30 30" aria-hidden="true"><path d="M4 16 L11 24 L27 5" fill="none" stroke="var(--tick-rust)" stroke-width="4" stroke-linecap="round" stroke-linejoin="round"/></svg>
      No Additives
    </li>
  </ul>

  <p class="freshness">fresh</p>
</body>
</html>
```